Web Design Project - Wallenbruck Homes

We would like you to refine our web layouts for a (1) homepage and (2) a product page (see attached files for reference).

The client is a swiss construction company, that designs, builds and sells standardized and tailored-made residential houses.

His logo is old, but not up for redesign. The only way to salvage it, is to incorporate its yellow color (as highlight) to the overall design, so as to create some brand awareness.

REQUIREMENTS FOR THE HOMEPAGE:
1. telephone number over menu
2. logo + menu with 6 categories
3. slider for showing various house types (for pics, see attachments)
4. "AKTUELL" card with yellow color (to show his most actual projects) and a strong Call For Action (what in German would be: KONTAKT AUFNEHMEN)
5. a yellow stripe for his company's slogan (Ihr Partner für individuelle und normierte Wohnbauten)
6. A left coloumn with
(a) two picture-holders under the title REFERENZEN
(b) the three supporting logos of TOVU, KALSOTEX and VR KLARWANDBAU VERBUND (can be downloaded as pngs)
7. A right column with 6 headlines + texts of 3 lines each
8. a footer with the adress info

REQUIREMENTS FOR PRODUKT PAGE:
1. slider for pictures
2. info box with Call For Action for particular House-types
3. thumbnail pics under the slider for additional images of any particular house type
4. Left-side: name of house type and picture
5. Right-side: Header and blindtext for house description
6. three placeholders for 3 floor plans

NB No coding necessary. An imaginative, fresh design along the layout requirements will do.
Thanx to all

To all those who had probs with the downloading of the attached files:
we've posted a new Zip.
Have a look!
thankx

Thanks to everyone who participated.
We will be showing a selection of your designs to the client within the next couple of days.
We'll get back to you, as soon as possible.

• - slider
- info box with call for action
- thumbnail pictures
- fresh look based on colors, design of elements (slider, info box), font selection

```html
<!DOCTYPE html>
<html lang="de">
<head>
<meta charset="utf-8">
<title>Wallenbruck Homes – Lausanne</title>
<link href="https://fonts.googleapis.com/css2?family=Cabin:wght@400;500&family=Oswald:wght@400&family=Arimo:wght@400;700&display=swap" rel="stylesheet">
<style>
:root{
  --yellow:#fdc800;
  --yellow-dark:#e9b400;
  --ink:#2f2f2f;
  --text:#555;
  --muted:#666;
  --line:#dcdcdc;
  --band:#d4d4d4;
  --page:#f3f3f1;
  --footer:#333333;
  --white:#fff;
}
*{margin:0;padding:0;box-sizing:border-box}
html,body{width:1108px;height:1200px;overflow:hidden}
body{position:relative;background:var(--page);font-family:"Arimo",Arial,sans-serif;color:var(--text)}
.abs{position:absolute}

.header{left:0;top:0;width:1108px;height:127px;background:linear-gradient(#f6f6f6,#fff)}
.brand{left:92px;top:58px;font-family:"Cabin",sans-serif;font-size:26px;font-weight:500;color:var(--ink);display:flex;align-items:center;gap:10px}
.brand-mark{width:16px;height:16px;background:var(--yellow)}
.phone{right:100px;top:40px;display:flex;align-items:center;gap:14px;font-family:"Oswald",sans-serif;font-size:21px;color:var(--ink);letter-spacing:.5px}
.phone-icon{width:24px;height:24px;background:#4b4f55;border-radius:4px;display:flex;align-items:center;justify-content:center}
.nav{left:350px;top:86px;display:flex;font-family:"Cabin",sans-serif;font-size:17px;color:var(--ink)}
.nav a{display:block;height:30px;line-height:30px;text-decoration:none;color:inherit}
.nav .active{background:var(--yellow);color:var(--white);padding:0 14px;margin-right:34px}
.nav .i2{margin-right:46px}.nav .i3{margin-right:58px}.nav .i4{margin-right:54px}.nav .i5{margin-right:50px}

.rule{left:0;top:127px;width:1108px;height:9px;background:var(--yellow)}
.stage{left:0;top:136px;width:1108px;height:337px;background:linear-gradient(var(--band),#ededec)}

.slider{left:93px;top:149px;width:656px;height:313px;background:var(--white);padding:4px}
.slider .photo{width:100%;height:100%;background:linear-gradient(#cfd9e2 0%,#b9a98f 45%,#5c7a3a 100%)}
.arrow{width:24px;height:24px;border-radius:50%;background:var(--white);display:flex;align-items:center;justify-content:center;box-shadow:0 1px 3px rgba(0,0,0,.35)}
.arrow.prev{left:124px;top:305px}.arrow.next{left:703px;top:303px}

.info-card{left:763px;top:149px;width:249px;height:314px;background:var(--white)}
.info-card h2{height:39px;background:var(--yellow);text-align:center;font-family:"Cabin",sans-serif;font-weight:400;font-size:22px;line-height:42px;color:var(--ink);border:1px solid #fff}
.specs{position:absolute;left:24px;top:53px;width:188px;font-size:11.5px;color:var(--muted)}
.specs .type{font-weight:700;padding:8px 12px 10px;border-bottom:1px dotted #555}
.specs .row{display:flex;padding:12px 12px 11px;border-bottom:1px dotted #ccc}
.specs .row:last-child{border-bottom:0}
.specs .row span:first-child{width:97px}
.cta{left:785px;top:419px;width:204px;height:33px;background:var(--yellow);border-radius:2px;display:flex;align-items:center;justify-content:space-between;padding:0 12px 0 15px;font-family:"Cabin",sans-serif;font-size:13px;color:var(--ink)}
.cta .arrow{position:static;width:23px;height:23px}

.thumbs{left:95px;top:497px;display:flex;gap:28px}
.thumb{width:69px;height:46px;background:linear-gradient(#cfd9e2,#a89a80 55%,#5f7d3c);border:1px solid #ccc}
.thumb.active{border:3px solid #111;width:71px;height:47px}

.content{left:92px;top:588px;width:922px;height:480px;background:linear-gradient(#fafaf9,#fff);border:1px solid #e4e4e4}
.content .title{left:24px;top:12px;font-family:"Cabin",sans-serif;font-size:16px;color:#555;letter-spacing:.5px}
.house-pic{left:24px;top:45px;width:176px;height:115px;border:2px solid #ccc;background:linear-gradient(#d2dbe3,#ad9e84 55%,#6b8a45)}
.desc{left:246px;top:50px;width:520px}
.desc h3{font-family:"Cabin",sans-serif;font-weight:400;font-size:16px;color:var(--ink);letter-spacing:.4px;margin-bottom:12px}
.desc p{font-size:11.2px;line-height:16.8px;color:#666}
.desc a{color:#6b6bd8;font-weight:700;margin-left:4px}
.plan{background:linear-gradient(#fdfdfd,#f0f0f0);border:1px solid #e2e2e2}
.plan-label{font-size:11.5px;color:#555}

.footer-rule{left:0;top:1075px;width:1108px;height:9px;background:var(--yellow)}
.footer{left:0;top:1084px;width:1108px;height:116px;background:var(--footer);color:var(--white);font-size:11px;font-weight:700;line-height:16.5px}
.footer .col{position:absolute;top:29px}
.footer-brand{right:96px;top:58px;font-family:"Cabin",sans-serif;font-size:15px;font-weight:500;color:#bdbdbd;display:flex;align-items:center;gap:8px}
.footer-brand i{width:10px;height:10px;background:#8a8a8a;display:block}
</style>
</head>
<body>

<header class="header abs">
  <div class="brand abs"><span class="brand-mark"></span>Wallenbruck Homes</div>
  <div class="phone abs">
    <span class="phone-icon"><svg width="14" height="14" viewBox="0 0 24 24"><path fill="#fff" d="M6.6 10.8a15 15 0 0 0 6.6 6.6l2.2-2.2c.3-.3.7-.4 1-.2 1.1.4 2.3.6 3.6.6.6 0 1 .4 1 1V20c0 .6-.4 1-1 1A17 17 0 0 1 3 4c0-.6.4-1 1-1h3.5c.6 0 1 .4 1 1 0 1.3.2 2.5.6 3.6.1.3 0 .7-.2 1z"/></svg></span>
    044 518 27 60
  </div>
  <nav class="nav abs">
    <a class="active">Home</a><a class="i2">Hauser</a><a class="i3">Renovatinen</a><a class="i4">Referenzen</a><a class="i5">Uber uns</a><a>Kontakt</a>
  </nav>
</header>

<div class="rule abs"></div>
<div class="stage abs"></div>

<div class="slider abs"><div class="photo" role="img" aria-label="Photo of a two-storey family house with stone facade and garage"></div></div>
<span class="arrow prev abs"><svg width="10" height="10" viewBox="0 0 10 10"><path d="M6.5 1.5 3 5l3.5 3.5" fill="none" stroke="#333" stroke-width="2"/></svg></span>
<span class="arrow next abs"><svg width="10" height="10" viewBox="0 0 10 10"><path d="M3.5 1.5 7 5 3.5 8.5" fill="none" stroke="#333" stroke-width="2"/></svg></span>

<aside class="info-card abs">
  <h2>LAUSANNE</h2>
  <div class="specs">
    <div class="type">EFH</div>
    <div class="row"><span>Umbauter Raum</span><span>655m2</span></div>
    <div class="row"><span>Bruttowohnflache</span><span>145m2</span></div>
    <div class="row"><span>Zimmer</span><span>1/2- 5 1/2</span></div>
    <div class="row"><span>abCHF</span><span>xxxxxx</span></div>
  </div>
</aside>
<div class="cta abs">KONTAKT AUFNEHMEN<span class="arrow"><svg width="10" height="10" viewBox="0 0 10 10"><path d="M3.5 1.5 7 5 3.5 8.5" fill="none" stroke="#333" stroke-width="2"/></svg></span></div>

<div class="thumbs abs">
  <div class="thumb active" role="img" aria-label="Thumbnail of house photo"></div>
  <div class="thumb" role="img" aria-label="Thumbnail of house photo"></div>
  <div class="thumb" role="img" aria-label="Thumbnail of house photo"></div>
  <div class="thumb" role="img" aria-label="Thumbnail of house photo"></div>
  <div class="thumb" role="img" aria-label="Thumbnail of house photo"></div>
  <div class="thumb" role="img" aria-label="Thumbnail of house photo"></div>
  <div class="thumb" role="img" aria-label="Thumbnail of house photo"></div>
</div>

<section class="content abs">
  <div class="title abs">LAUSANNE</div>
  <div class="house-pic abs" role="img" aria-label="Photo of the Lausanne house type"></div>
  <div class="desc abs">
    <h3>Bearatun and Betreuung</h3>
    <p>Lorem Ipsum is simply dummy text of the printing and typesetting industry. Lorem Ipsum has been the industry's standard dummy text ever since the 1500s, when an unknown printer took a galley of type and scrambled it to make a type specimen dummy text ever sinceever since the 1500s, <a>mehr...</a></p>
  </div>
  <div class="plan abs" style="left:26px;top:195px;width:196px;height:177px" role="img" aria-label="Floor plan of the basement"></div>
  <div class="plan-label abs" style="left:30px;top:391px">Untergeschoss</div>
  <div class="plan abs" style="left:274px;top:197px;width:192px;height:180px" role="img" aria-label="Floor plan of the ground floor"></div>
  <div class="plan-label abs" style="left:276px;top:404px">Erdgeschoss</div>
  <div class="plan abs" style="left:538px;top:197px;width:192px;height:180px" role="img" aria-label="Floor plan of the upper floor"></div>
  <div class="plan-label abs" style="left:540px;top:404px">Obergeschoss</div>
</section>

<div class="footer-rule abs"></div>
<footer class="footer abs">
  <div class="col" style="left:104px">WALLENBRUCK HOMES GMBH FAM.<br>BRENNER</div>
  <div class="col" style="left:373px">LINDENWEG 14 CH-8360<br>TALHEIM</div>
  <div class="col" style="left:568px">TEL . 044 518 2760<br>FAX . 044 518 2761</div>
  <div class="col" style="right:94px;top:24px">EMAIL : info@wallenbruck-homes.ch</div>
  <div class="footer-brand abs"><i></i>Wallenbruck Homes</div>
</footer>

</body>
</html>
```